Option Sheet

We need a one page option sheet with a left to right reading of the five options. It should be a one sheet, multiple colors and definitive separations between options This is used in a sales consultation. Backround or colors not in option need to have the follow RGB value (5 red, 20 green, 63 blue)

We added a smaller text file, please change that point

Target Market(s)

Divorce

Industry/Entity Type

Legal

Requirements
Must have
• 1) All five options left to right
• 2)language included in sheet

```html
<!DOCTYPE html>
<html lang="en">
<head>
<meta charset="utf-8">
<title>Five Options | Divorce</title>
<link href="https://fonts.googleapis.com/css2?family=Archivo:wght@700;800&family=Arimo:wght@400;700&display=swap" rel="stylesheet">
<style>
  :root{
    --backdrop:#e9edf3;
    --paper:#ffffff;
    --ink:#2b2b2b;
    --header:#2e2215;
    --navy:rgb(5,20,63);
    --teal-dark:#1d8a7f; --teal-light:#63c2b4;
    --orange-dark:#f39a45; --orange-light:#f9b57a;
    --purple-dark:#8c2a8a; --purple-light:#a955a3;
    --blue-dark:#4a5cad; --blue-light:#7282c2;
    --brown-dark:#5b4a3f; --brown-light:#d7b6a5;
  }
  *{box-sizing:border-box;margin:0;padding:0}
  html,body{width:1200px;height:1200px;overflow:hidden;background:var(--backdrop)}
  body{font-family:"Arimo",Arial,sans-serif;color:var(--ink)}
  .sheet{position:absolute;left:20px;top:190px;width:1160px;height:820px;background:var(--paper);overflow:hidden;box-shadow:0 10px 30px rgba(0,0,0,.15)}
  .sheet-header{position:absolute;left:28px;right:28px;top:22px;height:52px;background:var(--header);border-radius:26px 26px 0 0;color:#fff;font-size:27px;display:flex;align-items:center;justify-content:center;letter-spacing:.5px}
  .sheet-header strong{font-family:"Archivo",Arial,sans-serif;font-weight:800;margin-left:8px}
  .column{position:absolute;top:92px}
  .column-left{left:30px;width:540px}
  .column-right{left:600px;width:530px}
  .option{margin-bottom:14px}
  .option-head{display:flex;align-items:flex-end;height:42px}
  .option-tag{font-family:"Archivo",Arial,sans-serif;font-weight:800;color:#fff;font-size:16px;padding:6px 34px 5px 14px;clip-path:polygon(0 0,78% 0,100% 100%,0 100%);white-space:nowrap}
  .option-title{flex:1;position:relative;font-family:"Archivo",Arial,sans-serif;font-weight:800;font-size:21px;padding:0 0 9px 6px;border-bottom:9px solid}
  .option-icon{position:absolute;right:8px;bottom:10px;width:34px;height:34px}
  .band{font-family:"Archivo",Arial,sans-serif;font-weight:700;color:#fff;font-size:16px;letter-spacing:1px;padding:3px 14px;margin-top:0}
  .points{list-style:none;padding:6px 0 8px 28px;font-size:13px;line-height:17px}
  .points li{position:relative}
  .points li::before{content:"•";position:absolute;left:-16px}
  .opt-teal .option-tag{background:var(--teal-dark)} .opt-teal .option-title{color:var(--teal-dark);border-color:var(--teal-light)} .opt-teal .band{background:var(--teal-light)}
  .opt-orange .option-tag{background:var(--orange-dark)} .opt-orange .option-title{color:var(--orange-dark);border-color:var(--orange-light)} .opt-orange .band{background:var(--orange-light)}
  .opt-purple .option-tag{background:var(--purple-dark)} .opt-purple .option-title{color:var(--purple-dark);border-color:var(--purple-light)} .opt-purple .band{background:var(--purple-light)}
  .opt-blue .option-tag{background:var(--blue-dark)} .opt-blue .option-title{color:var(--blue-dark);border-color:var(--blue-light)} .opt-blue .band{background:var(--blue-light)}
  .opt-brown .option-tag{background:var(--brown-dark)} .opt-brown .option-title{color:var(--brown-dark);border-color:var(--brown-light)} .opt-brown .band{background:var(--brown-light)}
  .closing-rule{height:1px;background:var(--brown-light);margin-top:2px;width:100%}
  .bottom-wave{position:absolute;left:0;bottom:0;width:1160px;height:260px}
  .scene-art{position:absolute;left:800px;top:560px;width:330px;height:230px;border-radius:10px;background:linear-gradient(135deg,#b8c9d4 0%,#c9344f 50%,#e6c7b0 100%);opacity:.9}
</style>
</head>
<body>
<div class="sheet">
  <svg class="bottom-wave" viewBox="0 0 1160 260" preserveAspectRatio="none" aria-hidden="true">
    <path d="M0 190 C300 250 600 230 850 170 C980 140 1080 110 1160 95 L1160 260 L0 260 Z" fill="var(--navy)"/>
    <path d="M0 205 C320 255 620 225 860 175 C990 150 1090 125 1160 110" fill="none" stroke="#ffffff" stroke-opacity=".25" stroke-width="2"/>
  </svg>

  <div class="sheet-header">Five Options | <strong>Divorce</strong></div>

  <div class="column column-left">
    <section class="option opt-teal">
      <div class="option-head">
        <span class="option-tag">Option #1:</span>
        <h2 class="option-title">Do Nothing
          <svg class="option-icon" viewBox="0 0 34 34" aria-hidden="true"><rect x="5" y="6" width="24" height="26" rx="2" fill="none" stroke="var(--teal-dark)" stroke-width="3"/><rect x="12" y="2" width="10" height="7" rx="1" fill="var(--teal-dark)"/><path d="M12 15 L22 25 M22 15 L12 25" stroke="var(--teal-dark)" stroke-width="3"/></svg>
        </h2>
      </div>
      <div class="band">Advantages:</div>
      <ul class="points"><li>Stay married</li><li>No life Changes</li></ul>
      <div class="band">Disdvantages:</div>
      <ul class="points"><li>Money and assets may disappear</li><li>What is going to change?</li></ul>
    </section>

    <section class="option opt-orange">
      <div class="option-head">
        <span class="option-tag">Option #2:</span>
        <h2 class="option-title">Go to Counseling
          <svg class="option-icon" viewBox="0 0 34 34" aria-hidden="true" style="width:52px"><circle cx="8" cy="7" r="4" fill="var(--orange-dark)"/><rect x="4" y="12" width="8" height="11" rx="2" fill="var(--orange-dark)"/><path d="M2 20 V32 M2 26 H14 V32" stroke="var(--orange-dark)" stroke-width="2" fill="none"/><circle cx="26" cy="7" r="4" fill="var(--orange-dark)"/><rect x="22" y="12" width="8" height="11" rx="2" fill="var(--orange-dark)"/><path d="M32 20 V32 M32 26 H20 V32" stroke="var(--orange-dark)" stroke-width="2" fill="none"/></svg>
        </h2>
      </div>
      <div class="band">Advantages:</div>
      <ul class="points"><li>Reconcile marriage</li><li>Help make a better life</li></ul>
      <div class="band">Disadvantages:</div>
      <ul class="points"><li>Past issues are highlighted and may drudge up old wounds</li><li>It may just clarify the reasons you need to separate and/or divorce</li><li>Both parties must be invested and willing to participate</li></ul>
    </section>

    <section class="option opt-purple">
      <div class="option-head">
        <span class="option-tag">Option #3:</span>
        <h2 class="option-title">Do it Yourself
          <svg class="option-icon" viewBox="0 0 34 34" aria-hidden="true" style="width:48px"><circle cx="8" cy="5" r="3.5" fill="var(--purple-dark)"/><path d="M4 10 H12 L14 22 H2 Z" fill="var(--purple-dark)"/><rect x="5" y="22" width="2.5" height="10" fill="var(--purple-dark)"/><rect x="9" y="22" width="2.5" height="10" fill="var(--purple-dark)"/><circle cx="26" cy="5" r="3.5" fill="var(--purple-dark)"/><rect x="22" y="10" width="8" height="13" rx="1" fill="var(--purple-dark)"/><rect x="22.5" y="23" width="3" height="9" fill="var(--purple-dark)"/><rect x="26.5" y="23" width="3" height="9" fill="var(--purple-dark)"/><path d="M15 20 H20 L19 30 H16 Z" fill="none" stroke="var(--purple-dark)" stroke-width="1.5"/></svg>
        </h2>
      </div>
      <div class="band">Advantages:</div>
      <ul class="points"><li>No attorney fees</li><li>You are your on attorney</li></ul>
      <div class="band">Disadvantages:</div>
      <ul class="points"><li>People often find that what is “fair,” may in fact, not be truly fair</li><li>Often times, people do not know the risks</li><li>Complicated legal system within intrigue rules</li><li>Unsure how to complete the necessary paperwork and meet the deadlines</li></ul>
    </section>
  </div>

  <div class="column column-right">
    <section class="option opt-blue">
      <div class="option-head">
        <span class="option-tag">Option #4:</span>
        <h2 class="option-title">Limited Representation
          <svg class="option-icon" viewBox="0 0 34 34" aria-hidden="true"><circle cx="17" cy="9" r="7" fill="var(--blue-dark)"/><path d="M4 33 C4 22 9 18 17 18 C25 18 30 22 30 33 Z" fill="var(--blue-dark)"/><path d="M15 19 L17 28 L19 19 Z" fill="#fff"/></svg>
        </h2>
      </div>
      <div class="band">Advantages:</div>
      <ul class="points"><li>Balance between going alone and our limited involvement in the case</li></ul>
      <div class="band">Disadvantages:</div>
      <ul class="points"><li>Our terms may not benefit from our legal knowledge</li><li>The legal consequences of your legal documents will not be explained to you so that you can formulate a plan for handling the rest of your case.</li><li>Your spouse or other parties may cause your legal fees to increase significantly without action on your part</li></ul>
    </section>

    <section class="option opt-brown">
      <div class="option-head">
        <span class="option-tag">Option #5:</span>
        <h2 class="option-title">Hire Us
          <svg class="option-icon" viewBox="0 0 40 34" aria-hidden="true" style="width:44px"><circle cx="14" cy="9" r="7" fill="var(--brown-dark)"/><path d="M1 33 C1 22 6 18 14 18 C22 18 27 22 27 33 Z" fill="var(--brown-dark)"/><circle cx="30" cy="24" r="8" fill="var(--brown-dark)" stroke="#fff" stroke-width="1.5"/><path d="M26 24 L29 27 L34 21" stroke="#fff" stroke-width="2" fill="none"/></svg>
        </h2>
      </div>
      <div class="band">Advantages:</div>
      <ul class="points"><li>Gain the full benefits of our experience</li><li>Have a team of Family Law focus attorneys</li><li>Often saves you or makes you money in the long run</li><li>Save you time, energy and stress</li></ul>
      <div class="band">Disadvantages:</div>
      <ul class="points"><li>Initial cost</li></ul>
      <div class="closing-rule"></div>
    </section>
  </div>

  <div class="scene-art" role="img" aria-label="Illustration of a separated couple standing on either side of a large broken red heart"></div>
</div>
</body>
</html>
```